Photography Prints Business Card Design

Background info: Nature, flower, landscape,  macro, wildlife photographer. Shoot color and B&W images. Sell prints at juried fine art shows.
Looking for two-sided, clean, memorable design with creative use of my initials, DH.   I like the DH symbol in the my logo. Just use the DH symbol. Do not leave the underlying text as uploaded by me. I do not like the serif font and positioning of the words!  Either  remove the small print "Dorian Hallet Photography" under the logo,  or change to a sans serif font, or reposition with "Dorian Hallet" above "Photography" which seems to work with serif fonts.
Target Market(s)
Sophisticated art buyers, post-college to middle age
Industry/Entity Type
Business
Contact Information for Business Card
Dorian Hallet Photography
728 Maple Brook CT
Alder Crossing, OR 97999
(555) 010-0148
www.dorianhallet.com
CP:halletphoto
dorian@dorianhallet.com
If using just one line address, make sure there is a comma after  "CT" in street address. For example:
728 Maple Brook CT, Alder Crossing, OR 97999
Requirements
Must have
- 1.Two-sided card submitted as one design.
2. Must use the DH symbol in my logo.
3. Do not leave the text "Dorian Hallet Photography" under the DH symbol in the logo uploaded by me. I do not like that serif font or the positioning of the words! Either remove the small print "Dorian Hallet Photography" under the logo entirely, or change text to a sans serif font, or reposition text with "Dorian Hallet" above "Photography" which seems to work with serif fonts.
Nice to have
- Can use my DH logo (three file types uploaded: AI, PSD, TIF)  I  like the attached B&W water droplet photo.  My pictures on my website, www.dorianhhallet.com  can also be used.  Possible use of Chirply logo with (either the "f" alone or the square blue icon with white "f") my CP page short url name: halletphoto.
Should not have
- 1.No icons or pictures  of camera or lenses or other photographic gear or film strips.
2. No QR or other "barcode" type symbols.
3. No outlining of my logo symbol (drop shadow possibly).
4. No decorative or outlined fonts.
5. I am not a fan of most script fonts.
6. No play on "Hallet" such as snow or other winter season symbols.
7. Do not keep the original text, "Dorian Hallet Photography" under DH logo. Change it or remove it entirely.

```html
<!DOCTYPE html>
<html lang="en">
<head>
<meta charset="utf-8">
<title>Dorian Hallet Photography – Business Card</title>
<link rel="stylesheet" href="https://fonts.googleapis.com/css2?family=Barlow:wght@400;500&display=swap">
<style>
  :root {
    --backdrop: #3a322e;
    --card-white: #ffffff;
    --ink: #1c1c1c;
    --ink-soft: #3a3a3a;
    --rule: #222222;
    --photo-dark: #0b0b0b;
    --photo-mid: #5a5a5a;
    --photo-light: #b9b9b9;
    --badge: rgba(110, 110, 110, 0.75);
    --badge-text: #ffffff;
  }
  * { box-sizing: border-box; margin: 0; padding: 0; }
  html, body {
    width: 1200px;
    height: 716px;
    overflow: hidden;
    background: var(--backdrop);
    font-family: "Barlow", Arial, sans-serif;
  }
  .canvas {
    position: relative;
    width: 1200px;
    height: 716px;
  }
  .card {
    position: absolute;
    top: 215px;
    width: 500px;
    height: 286px;
    box-shadow: 0 10px 24px rgba(0, 0, 0, 0.45);
    overflow: hidden;
  }
  /* Front side */
  .card--front { left: 70px; background: var(--photo-dark); }
  .front__photo {
    position: absolute;
    inset: 0;
    background:
      radial-gradient(ellipse at 85% 40%, rgba(255,255,255,0.35), transparent 35%),
      linear-gradient(170deg, var(--photo-dark) 0%, var(--photo-dark) 28%, var(--photo-mid) 48%, var(--photo-light) 72%, var(--photo-mid) 100%);
  }
  .front__badge {
    position: absolute;
    left: 150px;
    top: 78px;
    width: 150px;
    height: 150px;
    border-radius: 50%;
    background: var(--badge);
    display: flex;
    align-items: center;
    justify-content: center;
    text-align: center;
  }
  .front__name {
    color: var(--badge-text);
    font-weight: 500;
    font-size: 17px;
    letter-spacing: 0.08em;
    text-transform: uppercase;
    line-height: 1.3;
  }
  /* Back side */
  .card--back { left: 630px; background: var(--card-white); }
  .back__brand {
    position: absolute;
    left: 12px;
    top: 0;
    width: 172px;
    height: 100%;
    display: flex;
    align-items: center;
    justify-content: flex-end;
  }
  .brand__name {
    color: var(--ink);
    font-weight: 500;
    font-size: 16px;
    letter-spacing: 0.1em;
    text-transform: uppercase;
    line-height: 1.4;
    text-align: right;
    white-space: nowrap;
  }
  .back__rule {
    position: absolute;
    left: 200px;
    top: 34px;
    width: 1.5px;
    height: 218px;
    background: var(--rule);
  }
  .back__contact {
    position: absolute;
    left: 218px;
    top: 50px;
    right: 12px;
    font-style: normal;
    color: var(--ink-soft);
    font-size: 13.5px;
    line-height: 1.3;
  }
  .contact__line { display: block; margin-bottom: 20px; white-space: nowrap; }
  .contact__line:last-child { margin-bottom: 0; }
</style>
</head>
<body>
  <main class="canvas">
    <section class="card card--front" aria-label="Card front">
      <div class="front__photo" role="img" aria-label="Black and white macro photograph of water droplets on a leaf"></div>
      <div class="front__badge">
        <span class="front__name">Dorian<br>Hallet</span>
      </div>
    </section>

    <section class="card card--back" aria-label="Card back">
      <div class="back__brand">
        <p class="brand__name">Dorian Hallet<br>Photography</p>
      </div>
      <div class="back__rule"></div>
      <address class="back__contact">
        <span class="contact__line">728 Maple Brook CT, Alder Crossing,<br>OR 97999</span>
        <span class="contact__line">(555) 010-0148</span>
        <span class="contact__line">www.dorianhallet.com</span>
        <span class="contact__line">CP:halletphoto dorian@dorianhallet.com</span>
      </address>
    </section>
  </main>
</body>
</html>
```